Business Card Design Project

I am looking for a business card design for my custom Audio/Video & Contracting business named Brelvora Systems Inc. We do not currently have a corporate logo so you should not feel constrained to work around an existing design. Your design should be elegant and clean while artistically conveying that we are a technology company. We provide A/V services for the commercial and residential markets and contracting services for residential remodeling and home theater construction. We do not have a particular color that we are looking to design around so feel free to be creative.

To get references of the kind of work that we do and design inspiration please visit the following sites:

http://www.quenlamark.us
www.morvethpro.com
www.feltonbraxa.com

Reason: I think we are getting close on a couple of the designs and want to give additional time to get tweaks done and to resubmit your designs.

Target Market(s)

Most of our clients are very wealthy and have been exposed to premium brand names in every aspect of their lives, (ie. - luxury autos, estate sized homes, fine jewelery and clothes) and your design needs to convey that same level of excellent design that they are used to.

Industry/Entity Type

Residential

Requirements
Should not have
• An extensive use of the color RED.

```html
<!DOCTYPE html>
<html lang="en">
<head>
<meta charset="utf-8">
<title>Brelvora Systems Inc. — Business Card</title>
<link href="https://fonts.googleapis.com/css2?family=Open+Sans:wght@300;400&display=swap" rel="stylesheet">
<style>
  :root {
    --navy: #0d2b80;
    --slate: #4f5d66;
    --paper: #ffffff;
    --backdrop: #e6e4e0;
    --ink-light: #ffffff;
  }
  html, body {
    margin: 0;
    padding: 0;
    width: 1200px;
    height: 1200px;
    overflow: hidden;
    background: var(--backdrop);
    font-family: "Open Sans", Arial, sans-serif;
  }
  .canvas {
    position: relative;
    width: 1200px;
    height: 1200px;
  }
  .card {
    position: absolute;
    left: 160px;
    width: 880px;
    height: 506px;
    background: var(--paper);
    overflow: hidden;
    box-shadow: 0 4px 14px rgba(0,0,0,0.18);
  }
  .card--front { top: 70px; }
  .card--back { top: 624px; background: var(--slate); }

  /* Front */
  .brand {
    position: absolute;
    top: 0; left: 0; right: 0;
    height: 182px;
    display: flex;
    align-items: center;
    justify-content: center;
    gap: 28px;
  }
  .brand__square {
    width: 96px;
    height: 96px;
    background: var(--navy);
    border-radius: 6px;
  }
  .brand__name {
    font-weight: 300;
    font-size: 58px;
    color: var(--navy);
    letter-spacing: 1px;
  }
  .rule {
    position: absolute;
    left: 0; right: 0;
    height: 8px;
    background: var(--navy);
  }
  .rule--top { top: 182px; }
  .rule--bottom { top: 452px; }
  .info-panel {
    position: absolute;
    top: 193px;
    left: 0; right: 0;
    height: 252px;
    background: var(--slate);
  }
  .person {
    position: absolute;
    left: 98px;
    top: 26px;
    color: var(--ink-light);
  }
  .person__name {
    font-size: 34px;
    font-weight: 400;
    line-height: 1.1;
  }
  .person__title {
    font-size: 21px;
    font-weight: 400;
    margin-top: 2px;
  }
  .person__email {
    margin-top: 26px;
    font-size: 21px;
    color: var(--navy);
  }
  .contact {
    position: absolute;
    right: 98px;
    top: 26px;
    text-align: right;
    font-size: 20px;
    font-weight: 300;
    line-height: 29px;
    color: var(--ink-light);
  }
  .contact__address { color: var(--navy); margin-bottom: 29px; }
  .contact__value { color: var(--navy); }
  .website {
    position: absolute;
    left: 0; right: 0;
    top: 460px;
    height: 46px;
    display: flex;
    align-items: center;
    justify-content: center;
    font-size: 26px;
    letter-spacing: 1px;
    color: var(--navy);
  }

  /* Back */
  .back-brand {
    position: absolute;
    left: 60px;
    top: 100px;
    width: 340px;
    display: flex;
    flex-direction: column;
    align-items: center;
    gap: 26px;
  }
  .back-brand__square {
    width: 150px;
    height: 150px;
    background: var(--ink-light);
    border-radius: 8px;
  }
  .back-brand__name {
    font-size: 40px;
    font-weight: 300;
    color: var(--ink-light);
  }
  .divider {
    position: absolute;
    left: 440px;
    top: 70px;
  }
  .services {
    position: absolute;
    left: 490px;
    top: 110px;
    margin: 0;
    padding: 0;
    list-style: none;
    color: var(--ink-light);
    font-size: 22px;
    line-height: 31px;
  }
  .back-band {
    position: absolute;
    left: 0; right: 0;
    top: 430px;
    height: 76px;
    background: var(--paper);
  }
  .back-band__rule {
    position: absolute;
    left: 0; right: 0;
    top: 4px;
    height: 7px;
    background: var(--navy);
  }
  .tagline {
    position: absolute;
    left: 0; right: 0;
    top: 11px;
    bottom: 0;
    display: flex;
    align-items: center;
    justify-content: center;
    padding-left: 120px;
    font-size: 23px;
    letter-spacing: 1px;
    color: var(--navy);
  }
</style>
</head>
<body>
<div class="canvas">

  <section class="card card--front">
    <header class="brand">
      <div class="brand__square"></div>
      <div class="brand__name">Brelvora Systems</div>
    </header>
    <div class="rule rule--top"></div>
    <div class="info-panel">
      <div class="person">
        <div class="person__name">Dorian Kessel</div>
        <div class="person__title">president</div>
        <div class="person__email">d.kessel@brelvorasystems.com</div>
      </div>
      <div class="contact">
        <div class="contact__address">482 Alder Lane<br>Toronto, ON Canada</div>
        <div>Dir: <span class="contact__value">+38 74 510 318</span></div>
        <div>Tel: <span class="contact__value">+38 74 510 377</span></div>
        <div>Mob: <span class="contact__value">+38 74 510 349</span></div>
        <div>Fax: <span class="contact__value">+38 74 510 302</span></div>
      </div>
    </div>
    <div class="rule rule--bottom"></div>
    <footer class="website">www.brelvorasystems.com</footer>
  </section>

  <section class="card card--back">
    <div class="back-brand">
      <div class="back-brand__square"></div>
      <div class="back-brand__name">Brelvora Systems</div>
    </div>
    <svg class="divider" width="4" height="280" viewBox="0 0 4 280" aria-hidden="true">
      <defs>
        <linearGradient id="divider-fade" x1="0" y1="0" x2="0" y2="1">
          <stop offset="0" stop-color="#ffffff" stop-opacity="0"/>
          <stop offset="0.4" stop-color="#ffffff" stop-opacity="0.9"/>
          <stop offset="1" stop-color="#ffffff" stop-opacity="0"/>
        </linearGradient>
      </defs>
      <rect x="1" y="0" width="2" height="280" fill="url(#divider-fade)"/>
    </svg>
    <ul class="services">
      <li>Media Distribution Systems</li>
      <li>Residential Remodeling</li>
      <li>Surround Sound</li>
      <li>Home Theater Construction</li>
      <li>Smart Home Control Systems</li>
    </ul>
    <div class="back-band">
      <div class="back-band__rule"></div>
      <div class="tagline">Audio/Video &amp; Contracting Services</div>
    </div>
  </section>

</div>
</body>
</html>
```